Create a banner for me that embodies my health and well being package.

I am an intuitive counselor with a busy practice helping clients to shift their blocks and move forward in their lives.
I have created a package called '9 paths home again'
I am wanting a banner to put on my website page, facebook page and to use as a letter head in mailouts.
My ideal clients are those who want to create change in their lives and who invest money in themselves and their personal and spiritual growth.
I am different to regular life coaches as my sessions have a spiritual twist to them creating much deeper change in my clients.
I would like the banner to be mainly font with the title of the progam: 9 Paths Home Again (no other wording) (something along the lines of the Blackjack font) and that ties in with the theme of my website. I'm not sure what else I want with it and am looking for ideas.
Website:
www.brightwillowhealing.com.au
I also have a current facebook page for the business:
https://www.facebook.com/Brightwillow-Healing-Studio-502718364091547/
(Note: I am about to drop my logo and business name and move to using my own name - the rest of the website will remain the same).
I have attached a doc with the draft of what wording will be on the website page any advertising will link to, to give you an idea of what the program is about.

Target Market(s)

People who invest money on themselves who are looking to improve their emotional well being and creating change in their life. Majority are middle aged women (also younger females and some men)

Industry/Entity Type

Health And Wellness

Font styles to use
Other font styles liked:
• I like Blackjack and Amienne. Along those lines.

Requirements
Must have
• Attractive, modern and GREAT font.
Nice to have
• Surprise me with something amazing!
• I love the colours in the 2 images I have up loaded as they represent the heart chakra colours. They could be a feature on the banner or blurred into the background.
Should not have
• Even though my work is quite spiritual I don't want it to look woo woo (meaning airy fairy spiritual stuff!)

```html
<!DOCTYPE html>
<html lang="en">
<head>
<meta charset="utf-8">
<title>9 paths home again – Balance and healing package</title>
<link rel="stylesheet" href="https://fonts.googleapis.com/css2?family=Oswald:wght@400&family=Open+Sans:wght@600&display=swap">
<style>
  :root {
    --leaf-deep: #2f5a12;
    --leaf-mid: #4f8a22;
    --leaf-light: #7cab3c;
    --lotus-pink: #e0559a;
    --lotus-soft: #f4a9cc;
    --pad-dark: #1f3a22;
    --text-white: #ffffff;
    --price-green: #cdf5a8;
  }
  * { margin: 0; padding: 0; box-sizing: border-box; }
  html, body {
    width: 1200px;
    height: 453px;
    overflow: hidden;
    background: var(--leaf-deep);
  }
  .banner {
    position: relative;
    width: 1200px;
    height: 453px;
    overflow: hidden;
  }
  .banner-photo {
    position: absolute;
    inset: 0;
    background:
      radial-gradient(ellipse 300px 230px at 300px 250px, var(--lotus-soft) 0%, var(--lotus-pink) 45%, rgba(224, 85, 154, 0) 100%),
      radial-gradient(ellipse 420px 90px at 300px 453px, var(--pad-dark) 0%, rgba(31, 58, 34, 0) 100%),
      radial-gradient(ellipse 260px 140px at 470px 60px, rgba(230, 200, 210, 0.55) 0%, rgba(230, 200, 210, 0) 100%),
      radial-gradient(ellipse 500px 300px at 900px 160px, var(--leaf-light) 0%, rgba(124, 171, 60, 0) 100%),
      linear-gradient(180deg, var(--leaf-mid) 0%, var(--leaf-deep) 100%);
  }
  .offer {
    position: absolute;
    left: 620px;
    top: 96px;
    width: 530px;
    text-align: center;
    color: var(--text-white);
    text-shadow: 0 1px 4px rgba(0, 0, 0, 0.25);
  }
  .offer-title {
    font-family: "Oswald", sans-serif;
    font-weight: 400;
    font-style: italic;
    font-size: 74px;
    line-height: 1;
    letter-spacing: 0.5px;
  }
  .offer-subtitle {
    margin-top: 20px;
    font-family: "Open Sans", sans-serif;
    font-weight: 600;
    font-size: 28px;
    line-height: 1;
  }
  .offer-price {
    margin-top: 22px;
    font-family: "Open Sans", sans-serif;
    font-weight: 600;
    font-size: 54px;
    line-height: 1;
    color: var(--price-green);
  }
</style>
</head>
<body>
  <div class="banner">
    <div class="banner-photo" role="img" aria-label="Photograph of a pink lotus flower in bloom on a dark lily pad, in front of a softly blurred green garden background"></div>
    <div class="offer">
      <h1 class="offer-title">9 paths home again</h1>
      <p class="offer-subtitle">Balance and healing package</p>
      <p class="offer-price">$1,695.00</p>
    </div>
  </div>
</body>
</html>
```